Ironvale Holdings Business card

We need a an amazing matte black and gold card! W are a finance investing company so we want something that's eye catching and sleek. We want it to be attractive and sleek and represent money. Heck with would like the letters and lgo to be printed as 24k gold one day. We have the logo added so please use the color scheme with the logo and have that beautifully placed on one side.

Target Market(s)

Investors of all ages

Industry/Entity Type

Financial

Contact Information for Business Card

Black and matte with gold lettering follow logo colrs please.

Font styles to use
Other font styles liked:
• you decide

Colors

Designer to choose colors to be used in the design.

Requirements
Must have
• Matte Black and Gold, logo on one side. job title and name , website, phone number and email address on the other side
Nice to have
• Matte black and crisp finish to attract investors
Should not have
• playful, very professional!

```html
<!DOCTYPE html>
<html lang="en">
<head>
<meta charset="utf-8">
<title>Ironvale Holdings — Business Card</title>
<link rel="stylesheet" href="https://fonts.googleapis.com/css2?family=Poppins:wght@400;500&display=swap">
<style>
  :root {
    --backdrop: #c9c6c5;
    --card-black: #141414;
    --gold-line: #dcbc3c;
    --gold-text: #b9a43c;
    --gold-brand: #d2b441;
  }
  * { margin: 0; padding: 0; box-sizing: border-box; }
  html, body {
    width: 1200px;
    height: 1200px;
    overflow: hidden;
    background: var(--backdrop);
  }
  .canvas {
    position: relative;
    width: 1200px;
    height: 1200px;
  }
  .card {
    position: absolute;
    left: 250px;
    width: 700px;
    height: 400px;
    background: var(--card-black);
  }
  .card--front { top: 147px; }
  .card--back { top: 652px; }
  .card__frame {
    position: absolute;
    inset: 0;
    width: 100%;
    height: 100%;
  }
  .card__frame line,
  .card__frame rect {
    stroke: var(--gold-line);
    stroke-width: 2;
    fill: none;
  }
  .brand {
    position: absolute;
    left: 0;
    right: 0;
    text-align: center;
    font-family: "Poppins", sans-serif;
    font-weight: 500;
    text-transform: uppercase;
    color: var(--gold-brand);
    line-height: 1;
    white-space: nowrap;
  }
  .brand--front {
    top: 180px;
    font-size: 40px;
    letter-spacing: 6px;
  }
  .brand--back {
    top: 78px;
    font-size: 22px;
    letter-spacing: 4px;
  }
  .contact {
    position: absolute;
    font-family: "Poppins", sans-serif;
    font-weight: 400;
    font-size: 17px;
    letter-spacing: -0.5px;
    text-transform: uppercase;
    color: var(--gold-text);
    line-height: 1;
    white-space: nowrap;
  }
  .contact--title { left: 98px; top: 219px; }
  .contact--name { left: 114px; top: 251px; }
  .contact--web { left: 459px; top: 217px; }
  .contact--phone { left: 462px; top: 252px; }
  .contact--email { left: 462px; top: 284px; }
</style>
</head>
<body>
<main class="canvas">

  <section class="card card--front" aria-label="Card front">
    <svg class="card__frame" viewBox="0 0 700 400" aria-hidden="true">
      <!-- outer frame -->
      <line x1="17" y1="17" x2="683" y2="17"/>
      <line x1="17" y1="383" x2="683" y2="383"/>
      <line x1="17" y1="17" x2="17" y2="124"/>
      <line x1="17" y1="273" x2="17" y2="383"/>
      <line x1="683" y1="17" x2="683" y2="124"/>
      <line x1="683" y1="273" x2="683" y2="383"/>
      <!-- inner frame -->
      <line x1="23" y1="26" x2="677" y2="26"/>
      <line x1="23" y1="374" x2="677" y2="374"/>
      <line x1="23" y1="26" x2="23" y2="124"/>
      <line x1="23" y1="273" x2="23" y2="374"/>
      <line x1="677" y1="26" x2="677" y2="124"/>
      <line x1="677" y1="273" x2="677" y2="374"/>
    </svg>
    <p class="brand brand--front">Ironvale Holdings</p>
  </section>

  <section class="card card--back" aria-label="Card back">
    <svg class="card__frame" viewBox="0 0 700 400" aria-hidden="true">
      <rect x="14" y="17" width="671" height="369"/>
      <line x1="352" y1="220" x2="352" y2="358"/>
    </svg>
    <p class="brand brand--back">Ironvale Holdings</p>
    <p class="contact contact--title">Job Title</p>
    <p class="contact contact--name">Name</p>
    <p class="contact contact--web">Website</p>
    <p class="contact contact--phone">Phone Number</p>
    <p class="contact contact--email">Email Address</p>
  </section>

</main>
</body>
</html>
```